Business Card Design

I am an Event and Wedding Planner in need of an eye catching business card featuring my logo (attached), my contact details, and my company tagline (Making every milestone simply magnificent...) I would like the tagline in font similar the logo's font.
Updates
I have just noticed that my logo has a misspelling so for the final design, I will be uploading a corrected logo as soon as I have it.
My apologies.
Reason: Waiting on a corrected logo...Occasions is misspelled and it should say Weddings not Wedding
The logo has been corrected so now Occasions is spelled correctly and it says Weddings instead of Wedding. Please use Edwardian Script ITC as the font for the tagline so it will match the logo. Thank you for your patience.
Target Market(s)
Engaged couples and people hosting milestone celebrations. 25-50 years old, predominately female
Industry/Entity Type
Business
Contact Information for Business Card
Rosalind Petty, Event Manager / Owner, Mobile: 0491 837 052, Email: rosalind@glimmerfieldevents.com.au, www.glimmerfieldevents.com.au, Making every milestone simply magnificent...

```html
<!DOCTYPE html>
<html lang="en">
<head>
<meta charset="utf-8">
<title>Glimmerfield Events – Business Card</title>
<link href="https://fonts.googleapis.com/css2?family=Playfair+Display:wght@400&family=Pinyon+Script&family=Federo&display=swap" rel="stylesheet">
<style>
  :root {
    --page: #ffffff;
    --silver-light: #fbfbfb;
    --silver-mid: #d9d9d9;
    --silver-dark: #8f8f8f;
    --ribbon: #f4f4f4;
    --ribbon-shade: #dcdcdc;
    --accent-teal: #bcd6d6;
    --red: #c0001c;
    --red-deep: #6e0010;
    --ink: #111111;
    --slate: #5f6b70;
    --white: #ffffff;
  }
  * { box-sizing: border-box; margin: 0; padding: 0; }
  html, body { width: 1200px; height: 1000px; overflow: hidden; background: var(--page); }
  .canvas { position: relative; width: 1200px; height: 1000px; }
  .card {
    position: absolute; top: 50px; width: 555px; height: 900px; overflow: hidden;
    box-shadow: 0 2px 6px rgba(0,0,0,.25);
  }
  .card--front { left: 34px; }
  .card--back { left: 622px; }
  .card__backdrop {
    position: absolute; inset: 0;
    background: radial-gradient(ellipse 55% 70% at 50% 60%, var(--silver-light) 0%, var(--silver-mid) 55%, var(--silver-dark) 100%);
  }
  .card--back .card__backdrop {
    background: radial-gradient(ellipse 60% 70% at 50% 45%, var(--silver-light) 0%, var(--silver-mid) 60%, var(--silver-dark) 100%);
  }
  .card__band { position: absolute; left: 0; top: 0; width: 555px; height: 900px; }
  .brand-name {
    position: absolute; left: 0; width: 100%; top: 330px; text-align: center;
    font-family: "Playfair Display", serif; font-size: 46px; color: var(--ink); line-height: 1.1;
  }
  .tagline {
    position: absolute; right: 38px; top: 700px; width: 340px; text-align: right;
    font-family: "Pinyon Script", cursive; font-size: 27px; line-height: 47px; color: var(--red);
  }
  .person { position: absolute; left: 268px; top: 592px; }
  .person__name {
    font-family: "Playfair Display", serif; font-size: 38px; color: var(--red);
    line-height: 1; transform: scaleX(.86); transform-origin: left;
  }
  .person__role {
    margin-top: 14px; font-family: "Playfair Display", serif; font-size: 24px;
    color: var(--slate); transform: scaleX(.86); transform-origin: left; white-space: nowrap;
  }
  .contact { position: absolute; left: 72px; top: 736px; list-style: none; }
  .contact__item {
    display: flex; align-items: center; height: 37px;
    font-family: "Federo", sans-serif; font-size: 19px; color: var(--white);
  }
  .contact__icon { width: 30px; height: 26px; margin-right: 12px; }
</style>
</head>
<body>
<main class="canvas">

  <section class="card card--front" aria-label="Card front">
    <div class="card__backdrop" role="img" aria-label="Silver gradient background with scattered confetti"></div>
    <h1 class="brand-name">Glimmerfield Events</h1>
    <svg class="card__band" viewBox="0 0 555 900" aria-hidden="true">
      <defs>
        <radialGradient id="redFront" cx="50%" cy="10%" r="90%">
          <stop offset="0" stop-color="var(--red)"/>
          <stop offset="1" stop-color="var(--red-deep)"/>
        </radialGradient>
      </defs>
      <rect x="0" y="748" width="555" height="152" fill="url(#redFront)"/>
      <polygon points="0,725 180,725 290,688 555,688 555,793 96,793 56,750 0,750" fill="var(--ribbon)"/>
      <polygon points="0,725 180,725 172,732 0,732" fill="var(--ribbon-shade)"/>
      <polygon points="180,725 210,712 176,742" fill="var(--accent-teal)"/>
      <polygon points="40,736 56,750 48,750" fill="var(--accent-teal)"/>
    </svg>
    <p class="tagline">Making every milestone<br>simply magnificent...</p>
  </section>

  <section class="card card--back" aria-label="Card back">
    <div class="card__backdrop" role="img" aria-label="Silver gradient background with fine diagonal stripes"></div>
    <svg class="card__band" viewBox="0 0 555 900" aria-hidden="true">
      <defs>
        <radialGradient id="redBack" cx="50%" cy="25%" r="85%">
          <stop offset="0" stop-color="var(--red)"/>
          <stop offset="1" stop-color="var(--red-deep)"/>
        </radialGradient>
      </defs>
      <rect x="0" y="645" width="555" height="255" fill="url(#redBack)"/>
      <polygon points="0,622 150,622 273,582 555,582 555,690 95,690 50,647 0,647" fill="var(--ribbon)"/>
      <polygon points="0,622 150,622 142,630 0,630" fill="var(--ribbon-shade)"/>
      <polygon points="150,622 205,600 152,650" fill="var(--accent-teal)"/>
      <polygon points="36,634 50,647 42,647" fill="var(--accent-teal)"/>
    </svg>
    <div class="person">
      <h2 class="person__name">Rosalind Petty</h2>
      <p class="person__role">Event Manager / Owner</p>
    </div>
    <ul class="contact">
      <li class="contact__item">
        <svg class="contact__icon" viewBox="0 0 30 26" aria-hidden="true"><rect x="8" y="2" width="14" height="22" rx="2.5" fill="none" stroke="#fff" stroke-width="2.4"/><circle cx="15" cy="20" r="1.5" fill="#fff"/></svg>
        0491 837 052
      </li>
      <li class="contact__item">
        <svg class="contact__icon" viewBox="0 0 30 26" aria-hidden="true"><rect x="2" y="5" width="26" height="16" fill="#fff"/><polyline points="2,5 15,15 28,5" fill="none" stroke="#b00018" stroke-width="2"/><line x1="2" y1="21" x2="12" y2="13" stroke="#b00018" stroke-width="1.5"/><line x1="28" y1="21" x2="18" y2="13" stroke="#b00018" stroke-width="1.5"/></svg>
        rosalind@glimmerfieldevents.com.au
      </li>
      <li class="contact__item">
        <svg class="contact__icon" viewBox="0 0 30 26" aria-hidden="true"><circle cx="15" cy="13" r="12" fill="#fff"/><g fill="none" stroke="#b00018" stroke-width="1.4"><ellipse cx="15" cy="13" rx="5" ry="12"/><line x1="15" y1="1" x2="15" y2="25"/><line x1="3" y1="13" x2="27" y2="13"/><line x1="5" y1="7" x2="25" y2="7"/><line x1="5" y1="19" x2="25" y2="19"/></g></svg>
        www.glimmerfieldevents.com.au
      </li>
    </ul>
  </section>

</main>
</body>
</html>
```